Startup Consultancy - Brochure Design

This needs to be a digital and potential hardcopy of a glossy brochure, designed to really catch the eye of prospective clients and draw them in. I am looking for something alternative from the "usual", but equally in keeping with the IT industry that the business operate in. The business specifically focuses on Print & Document Software and Technology solutions, and this should be considered in the design.

Target Market(s)

SMB and Corporate End Users, + Technology Resellers

Industry/Entity Type

Information Technology

Other font styles liked:
• Avenir

Colors
9d9d9d
848484
c3c3c3
e8e8e8
ffffff
eaeaea
0255a3
3176b5
85acd3

Requirements
Must have
• Company logo displayed on the front, plus any other relevant placements in pages
• Must follow the colour/style in some way of the website (www.brantwellconsultancy.co.uk)
Nice to have
• Some kind of infographical style in the brochure would be good, perhaps around the service listings

```html
<!DOCTYPE html>
<html lang="en">
<head>
<meta charset="utf-8">
<title>Brantwell Consultancy – Brochure Cover</title>
<link rel="stylesheet" href="https://fonts.googleapis.com/css2?family=Nunito+Sans:wght@700;800;900&display=swap">
<style>
  :root {
    --stage: #e8e8e8;
    --brand-blue: #3176b5;
    --deep-blue: #0255a3;
    --ink: #2b2b2b;
    --white: #ffffff;
    --photo-warm: #f1c9a0;
    --photo-cream: #f6e2c8;
    --photo-rust: #a5624a;
    --photo-blue: #2f5d93;
    --photo-haze: #9bb3cf;
  }
  html, body {
    margin: 0;
    padding: 0;
    width: 1200px;
    height: 1200px;
    overflow: hidden;
    background: var(--stage);
    font-family: "Nunito Sans", "Avenir", sans-serif;
  }
  .canvas {
    position: relative;
    width: 1200px;
    height: 1200px;
    display: flex;
    align-items: center;
    justify-content: center;
  }
  .cover {
    position: relative;
    width: 560px;
    height: 1120px;
    overflow: hidden;
    box-shadow: 0 18px 40px rgba(0, 0, 0, 0.18);
  }
  .cover__photo {
    position: absolute;
    inset: 0;
    background:
      radial-gradient(ellipse 60% 30% at 95% 8%, var(--photo-rust) 0%, rgba(165, 98, 74, 0) 100%),
      radial-gradient(ellipse 50% 25% at 10% 10%, var(--photo-haze) 0%, rgba(155, 179, 207, 0) 100%),
      linear-gradient(180deg,
        var(--photo-warm) 0%,
        var(--photo-cream) 30%,
        #d9c6b8 52%,
        #8ea4c2 72%,
        var(--photo-blue) 100%);
  }
  .brand {
    position: absolute;
    left: 62px;
    top: 150px;
    display: flex;
    align-items: center;
    gap: 12px;
  }
  .brand__mark {
    width: 22px;
    height: 22px;
    background: var(--ink);
  }
  .brand__name {
    font-weight: 800;
    font-size: 34px;
    color: var(--ink);
    letter-spacing: 0.5px;
  }
  .headline {
    position: absolute;
    left: 52px;
    top: 268px;
    margin: 0;
    font-weight: 900;
    font-size: 56px;
    line-height: 62px;
    color: var(--brand-blue);
    text-transform: uppercase;
    letter-spacing: 1px;
  }
  .intro {
    position: absolute;
    left: 54px;
    top: 456px;
    width: 470px;
    margin: 0;
    font-weight: 800;
    font-size: 29px;
    line-height: 51px;
    color: var(--white);
    text-transform: uppercase;
    letter-spacing: 1.5px;
  }
</style>
</head>
<body>
  <main class="canvas">
    <section class="cover">
      <div class="cover__photo" role="img" aria-label="Photograph of an office desk with an open laptop and a potted plant, washed in warm light fading to blue"></div>

      <div class="brand">
        <span class="brand__mark"></span>
        <span class="brand__name">Brantwell</span>
      </div>

      <h1 class="headline">Welcome<br>to a new<br>approach</h1>

      <p class="intro">We have a range<br>of services<br>suitable for a<br>range of clients<br>including end users,<br>channel partners,<br>OEM's and distributors.</p>
    </section>
  </main>
</body>
</html>
```